Sports Nutrition Supplement Label design

We need a sports supplement label design for an existing business. (I have provided our business logo in the file uploads) These labels will remain consistent across the product line with the name of the product being the only changing field. The current product names (example: "vegan") on the labels provided are just for reference, the ingredients portions etc are final, but the actual name will be changed to something less generic for each product. I will just need to be able to change the name and have it match with label concept. We would like the look to be professional, clean, and exemplify quality. Please reference our business website tidelinevigor.com to get a feel for design and brand association.
I have also included the NKB supplement label guidelines so we are certain to maintain compliance.
Thank you and I'm looking forward to working with you and seeing your creative designs!
Darin

Target Market(s)

Athletes, Sports professionals, Colleges, Professional Sports Teams

Industry/Entity Type

Sports Science/ Sports Training/Athletics

Requirements
Nice to have
• I would like the design to possibly reflect these key terms: Sport Science, Chemistry, Clean, Professional, Quality (We also like water/ocean/waves concepts but is not a "requirement" it would have to really work well in the design somehow to appeal to wide range of athletes)

```html
<!DOCTYPE html>
<html lang="en">
<head>
<meta charset="utf-8">
<title>Tideline Vigor – Supplement Label Range</title>
<link rel="stylesheet" href="https://fonts.googleapis.com/css2?family=Josefin+Sans:wght@600&family=Open+Sans:wght@400;600;700;800&display=swap">
<style>
  :root {
    --page-bg: #ffffff;
    --label-bg: #ffffff;
    --ink-dark: #262626;
    --ink-body: #1e1e1e;
    --flavor-brown: #8b5a2b;
    --brand-text: #f2f2f2;
    --vit-blue: #1f5fb8;
    --vit-blue-light: #7fb4ea;
    --vit-cyan: #2fa7dd;
    --vit-green: #3c9a3a;
    --purple: #7a2a85;
    --purple-light: #b57bbd;
    --green: #1f8f46;
    --green-light: #64bf84;
    --blue: #2263ad;
    --blue-light: #5f9ad6;
  }
  * { box-sizing: border-box; margin: 0; padding: 0; }
  html, body {
    width: 1200px; height: 840px; overflow: hidden;
    background: var(--page-bg);
    font-family: "Open Sans", sans-serif;
  }
  .label-range {
    position: relative; width: 1200px; height: 840px;
    display: flex; justify-content: center; align-items: center; gap: 36px;
  }
  .label {
    position: relative; width: 340px; height: 420px;
    background: var(--label-bg);
    overflow: hidden;
    box-shadow: 0 2px 14px rgba(0,0,0,0.12);
  }
  .label--purple { --accent: var(--purple); --accent-light: var(--purple-light); }
  .label--green  { --accent: var(--green);  --accent-light: var(--green-light); }
  .label--blue   { --accent: var(--blue);   --accent-light: var(--blue-light); }

  .brand-box {
    position: absolute; top: 0; left: 62px; width: 216px; height: 128px;
    border-radius: 0 0 24px 24px;
    background: linear-gradient(90deg, var(--accent-light), var(--accent) 55%);
    display: flex; flex-direction: column; justify-content: center; align-items: center;
    font-family: "Josefin Sans", sans-serif; font-weight: 600;
    font-size: 30px; line-height: 1.1; letter-spacing: 3px;
    color: var(--brand-text);
  }
  .vitamin {
    position: absolute; border-radius: 50%;
    display: flex; justify-content: center; align-items: center;
    color: #fff; font-weight: 700;
  }
  .vitamin--a  { top: 56px; left: 10px; width: 30px; height: 42px; font-size: 20px;
                 background: radial-gradient(circle at 40% 35%, var(--vit-blue-light), var(--vit-blue)); }
  .vitamin--fe { top: 56px; right: 10px; width: 28px; height: 42px; font-size: 18px;
                 background: radial-gradient(circle at 40% 35%, var(--vit-blue), #10307a); }
  .vitamin--e  { top: 150px; left: 4px; width: 16px; height: 30px; font-size: 12px;
                 background: var(--vit-cyan); }
  .vitamin--b  { top: 168px; right: 4px; width: 16px; height: 30px; font-size: 12px;
                 background: var(--vit-green); }

  .product-name {
    position: absolute; top: 142px; left: 0; width: 100%;
    text-align: center;
    font-weight: 800; font-size: 84px; line-height: 1; letter-spacing: 1px;
    color: var(--ink-dark);
  }
  .texture-field {
    position: absolute; left: 0; right: 0; top: 236px; height: 136px;
    background: linear-gradient(180deg, rgba(255,255,255,0), color-mix(in srgb, var(--accent-light) 35%, white));
  }
  .athlete-figure {
    position: absolute; left: 0; top: 222px; width: 36px; height: 124px;
    background: var(--accent); opacity: 0.85;
    border-radius: 0 18px 18px 0;
  }
  .flavor {
    position: absolute; top: 262px; left: 30px; right: 10px;
    text-align: center;
    font-weight: 700; font-size: 22px; letter-spacing: 0.2px;
    color: var(--flavor-brown);
  }
  .flavor-note {
    position: absolute; top: 296px; left: 30px; right: 10px;
    text-align: center;
    font-weight: 400; font-size: 18px; color: var(--ink-body);
  }
  .net-pill {
    position: absolute; top: 334px; left: 48px; width: 252px; height: 26px;
    border-radius: 13px; background: var(--accent);
    display: flex; justify-content: center; align-items: center; gap: 6px;
    color: #fff; font-weight: 600; font-size: 10px;
  }
  .net-pill .divider { width: 1px; height: 14px; background: #fff; }
  .base-band {
    position: absolute; left: 0; right: 0; bottom: 0; height: 34px;
    background: linear-gradient(90deg, var(--accent-light), var(--accent) 40%);
  }
</style>
</head>
<body>
<main class="label-range">

  <section class="label label--purple">
    <div class="texture-field"></div>
    <div class="brand-box"><span>TIDELINE</span><span>VIGOR</span></div>
    <span class="vitamin vitamin--a">A</span>
    <span class="vitamin vitamin--fe">Fe</span>
    <span class="vitamin vitamin--e">E</span>
    <span class="vitamin vitamin--b">B</span>
    <h1 class="product-name">VEGAN</h1>
    <div class="athlete-figure" role="img" aria-label="Running athlete silhouette"></div>
    <p class="flavor">CHOCOLATE MILKSHAKE</p>
    <p class="flavor-note">Natural&nbsp; Flavor</p>
    <div class="net-pill"><span>NET WT. 907 G (2 LB)</span><span class="divider"></span><span>DIETARY SUPPLEMENT</span></div>
    <div class="base-band"></div>
  </section>

  <section class="label label--green">
    <div class="texture-field"></div>
    <div class="brand-box"><span>TIDELINE</span><span>VIGOR</span></div>
    <span class="vitamin vitamin--a">A</span>
    <span class="vitamin vitamin--fe">Fe</span>
    <span class="vitamin vitamin--e">E</span>
    <span class="vitamin vitamin--b">B</span>
    <h1 class="product-name">VEGAN</h1>
    <div class="athlete-figure" role="img" aria-label="Running athlete silhouette"></div>
    <p class="flavor">CHOCOLATE MILKSHAKE</p>
    <p class="flavor-note">Natural&nbsp; Flavor</p>
    <div class="net-pill"><span>NET WT. 907 G (2 LB)</span><span class="divider"></span><span>DIETARY SUPPLEMENT</span></div>
    <div class="base-band"></div>
  </section>

  <section class="label label--blue">
    <div class="texture-field"></div>
    <div class="brand-box"><span>TIDELINE</span><span>VIGOR</span></div>
    <span class="vitamin vitamin--a">A</span>
    <span class="vitamin vitamin--fe">Fe</span>
    <span class="vitamin vitamin--e">E</span>
    <span class="vitamin vitamin--b">B</span>
    <h1 class="product-name">VEGAN</h1>
    <div class="athlete-figure" role="img" aria-label="Running athlete silhouette"></div>
    <p class="flavor">CHOCOLATE MILKSHAKE</p>
    <p class="flavor-note">Natural&nbsp; Flavor</p>
    <div class="net-pill"><span>NET WT. 907 G (2 LB)</span><span class="divider"></span><span>DIETARY SUPPLEMENT</span></div>
    <div class="base-band"></div>
  </section>

</main>
</body>
</html>
```